Plakat-Design für Softwareentwicklung im Automotive-Sektor
Zielgruppe
Softwareentwicklung im Automotive-Sektor
Aufgabenstellung
Guten Tag,
wir benötigen ein Design für die Standwände und die Infotheke (LED-beleuchtet) unseres Messestandes auf einer Automotive Fachmesse.
Druckdaten, ein Layout unseres Standes und alle weiteren nötigen Daten finden Sie im Upload.
Im Upload finden Sie auch unser Signature Bild, das in das Design eingearbeitet werden soll - beispielsweise auf der Rückwand und die Seitenwände werden mit Logo/Slogan/einfarbig passend gestaltet oder Sie binden das Bild ganz ein - wir sind offen und gespannt auf Ihre Vorschläge!)
Außerdem finden Sie im Upload unser Firmenlogo samt Slogan 'Enter perfect Engineering.'
Unsere Website, um einen Eindruck vom Corporate Design zu erhalten:
https://www.voltarisnet.de/de/
Wir freuen uns auf Ihre Designs!

```html
<!DOCTYPE html>
<html lang="de">
<head>
<meta charset="utf-8">
<title>VoltarisNet – Messestand Entwurf</title>
<link rel="stylesheet" href="https://fonts.googleapis.com/css2?family=Arimo:wght@400&family=Oswald:wght@300;400&display=swap">
<style>
  :root {
    --bg-top: #5e5e60;
    --bg-mid: #87898b;
    --bg-bottom: #606062;
    --heading: #343434;
    --panel-dark: #464646;
    --panel-white: #ffffff;
    --teal: #0f8b82;
    --orange: #f07f1e;
    --light-type: #e4e4e4;
    --tagline: #6b6b6b;
    --seam: #6f7073;
  }
  * { margin: 0; padding: 0; box-sizing: border-box; }
  html, body { width: 1200px; height: 3844px; overflow: hidden; }
  body {
    position: relative;
    background: linear-gradient(180deg, var(--bg-top) 0%, var(--bg-mid) 45%, var(--bg-mid) 60%, var(--bg-bottom) 100%);
    font-family: "Oswald", sans-serif;
  }
  .view-title {
    position: absolute; left: 0; width: 1200px; text-align: center;
    font-family: "Arimo", sans-serif; font-size: 80px; color: var(--heading);
    line-height: 1;
  }
  .panel { position: absolute; background: var(--panel-dark); overflow: hidden; }
  .panel-header { position: absolute; left: 0; top: 0; width: 100%; background: var(--panel-white); }

  /* front counter */
  .front { left: 251px; top: 219px; width: 698px; height: 654px; }
  .front .panel-header { height: 121px; border-top: 6px solid var(--teal); }
  .front .brand {
    position: absolute; left: 0; width: 100%; top: 14px; text-align: center;
    font-size: 58px; font-weight: 300; color: var(--teal); letter-spacing: -0.5px;
  }
  .front .brand-dot {
    display: inline-block; width: 40px; height: 40px; background: var(--teal);
    margin-left: 12px; vertical-align: -2px;
  }
  .front .tagline {
    position: absolute; left: 168px; top: 84px; font-size: 19px; font-weight: 300; color: var(--tagline);
  }
  .front .visual { position: absolute; left: 0; top: 121px; }
  .slogan {
    position: absolute; font-size: 48px; line-height: 67px; font-weight: 400; text-transform: uppercase;
  }
  .front .slogan { left: 471px; top: 148px; color: var(--orange); }

  /* side wall */
  .side { left: 433px; top: 1097px; width: 334px; height: 646px; }
  .side .panel-header { height: 109px; }
  .side .seam { position: absolute; left: 0; width: 100%; height: 8px; background: var(--seam); }
  .side .brand-stack {
    position: absolute; left: 0; width: 100%; top: 176px; text-align: center;
    color: var(--light-type); font-size: 66px; font-weight: 300; line-height: 62px;
  }
  .side .brand-square {
    display: block; width: 70px; height: 70px; margin: 0 auto 26px; background: var(--light-type);
  }

  /* back wall */
  .back { left: 251px; top: 1967px; width: 698px; height: 649px; }
  .back .panel-header { height: 115px; }
  .back .brand {
    position: absolute; left: 93px; top: 176px; font-size: 78px; font-weight: 300; color: var(--light-type);
  }
  .back .brand-dot {
    display: inline-block; width: 56px; height: 56px; background: var(--light-type); margin-left: 16px; vertical-align: -4px;
  }
  .back .slogan { left: 207px; top: 330px; color: var(--light-type); }

  .booth-render { position: absolute; left: 21px; top: 2818px; width: 1158px; height: 861px; }
</style>
</head>
<body>
  <h2 class="view-title" style="top:78px">Zuhause</h2>
  <section class="panel front">
    <div class="panel-header">
      <div class="brand">VoltarisNet<span class="brand-dot"></span></div>
      <div class="tagline">Enter perfect Engineering.</div>
    </div>
    <svg class="visual" width="698" height="533" viewBox="0 0 698 533">
      <defs>
        <linearGradient id="roads" x1="0" y1="0" x2="1" y2="1">
          <stop offset="0" stop-color="#3a3a3a"/>
          <stop offset="0.45" stop-color="#6a5a48"/>
          <stop offset="0.6" stop-color="#9a6a34"/>
          <stop offset="1" stop-color="#2b2b2b"/>
        </linearGradient>
      </defs>
      <path role="img" aria-label="Nachtaufnahme geschwungener Autobahnkreuze mit orangefarbenen Lichtspuren"
            d="M0 0 H376 Q520 250 264 533 H0 Z" fill="url(#roads)"/>
      <path d="M376 0 Q520 250 264 533" fill="none" stroke="var(--orange)" stroke-width="16"/>
    </svg>
    <div class="slogan">Enter<br>Perfect<br>Enginering</div>
  </section>

  <h2 class="view-title" style="top:948px">Seite</h2>
  <section class="panel side">
    <div class="panel-header"></div>
    <div class="seam" style="top:109px"></div>
    <div class="brand-stack"><span class="brand-square"></span>Voltaris<br>Net</div>
    <div class="seam" style="top:524px"></div>
  </section>

  <h2 class="view-title" style="top:1820px">der Rücken</h2>
  <section class="panel back">
    <div class="panel-header"></div>
    <div class="brand">VoltarisNet<span class="brand-dot"></span></div>
    <div class="slogan">Enter<br>Perfect<br>Enginering</div>
  </section>

  <svg class="booth-render" viewBox="0 0 1158 861" role="img"
       aria-label="Visualisierung des Messestandes mit Seitentürmen, Rückwand, Sitzgruppe und beleuchteter Infotheke">
    <defs>
      <linearGradient id="booth" x1="0" y1="0" x2="0" y2="1">
        <stop offset="0" stop-color="#d6d6d6"/>
        <stop offset="0.7" stop-color="#bdbdbd"/>
        <stop offset="1" stop-color="#9c9c9c"/>
      </linearGradient>
    </defs>
    <rect width="1158" height="861" fill="url(#booth)"/>
  </svg>
</body>
</html>
```